Infografik/ Zeitleiste für Startup
Zielgruppe
Wir sind ein Startup, das über die Seite Zeitwabe.de zukünftig folgenden Service anbietet: Unternehmer können sehr flexibel (selbst) gestaltete Terminformulare erstellen und auf Ihrer Website einbinden. Kunden können dann diese Termine buchen und bekommen dann Erinnerungs-Mails und SMS.
Zielgruppe: Dienstleister wie Fotografen, Friseure, Versicherungsvertreter, Masseure, Restaurants, Arztpraxen. Also alle, die darauf angewiesen sind, dass vereinbarte Termine eingehalten werden und die die Terminvereinbarung vereinfachen wollen. Also weniger per Telefon, mehr über die eigene Website.
Zeitwabe ist mit LobPunkt.com (aktuell noch Top-und-Flop.com) verknüpft. Kunden, die einen Termin wünschen, sehen die Bewertungen vorheriger Kunden. Das stärkt das Vertrauen und erhöht die Termin-Zuverlässigkeit (Verbessert die No-Show-Rate). Damit sinken auch die Werbekosten je Kunden (geringere Kosten pro Conversion).
Zeitwabe.de und LobPunkt.com (aktuell noch Top-und-Flop.com) wurde vom Team von Bild-Kontor.de entwickelt. Dank Zeitwabe und LobPunkt.com haben wir (das Team von Bild-Kontor.de) folgende Vorteile:
- verbesserte Termin-Zuverlässigkeit (No-Show-Rate)
- mehr Kunden, mehr Shootings
- höherer Umsatz
- Zeitersparnis bei der Terminvereinbarung
- Senkungen der Werbekosten je Kunden (geringere Kosten pro Conversion)
Das ist der Grund, warum wir Zeitwabe und LobPunkt nun auch für andere Branchen anbieten.
Siehe auch: https://www.videoportal-beispiel.de/watch?v=qRtmZZk_31p
Siehe auch: https://www.videoportal-beispiel.de/watch?v=wLpoNNe_74x
Aufgabenstellung
Wir benötigen für Zeitwabe.de eine Infografik. Diese soll verdeutlichen, welche Vorteile wir (Bild-Kontor.de) dank Zeitwabe und LobPunkt haben:
Der Betrachter soll diese Zahlen auf einen Blick werten und die Vorteile für SEIN GESCHÄFT erkennen können. Zum Beispiel anhand einer Zeitleiste, die die Entwicklung der verschiedenen Kennzahlen wiedergibt.
Die Kennzahlen (die Entwicklung) können Sie hier aufrufen: https://ablage-beispiel.de/ordner/7KrtWmPq2ZxN8-vbYy3HsLd0QaTeRcU?teilen=ja
Besonders soll die positive Entwicklung ab Ende September 2017 deutlich werden. Ab Ende September 2017 haben wir Zeitwabe und LobPunkt.com für die Terminvereinbarung genutzt. Vorher haben wir Termine per Email und Telefon vereinbart, was deutlich zeitintensiver war.
Das Design der Zeitleiste (der Infografik) soll sich an Zeitwabe.de orientieren.
Falls die sechs Kennzahlen nicht übersichtlich in einer Zeitleiste darstellbar sind, könnten die Kennzahlen auf mehrere Grafiken aufgeteilt werden.
Vorstellbar ist auch eine interaktive Infografik, bei der man die jeweilige Kennzahl auswählen kann.
Wir lassen uns hier gerne von Ihrer Kreativität überraschen. Der spätere Kunde/Nutzer/ Betrachter der Infografik steht bitte im Vordergrund jeder Überlegung/jedes Designs.
Nutzen Sie ggf. bitte Icons und verschiedenen Farben, um die verschiedenen Kennzahlen auch visuell zu verdeutlichen.
Die Infografik soll später auf https://entwickler.zeitwabe.de/de/ueber-uns.html und in Flyern veröffentlicht werden.
Wesentliche Funktionen und Vorteile siehe auch:
https://www.videoportal-beispiel.de/watch?v=qRtmZZk_31p
https://www.videoportal-beispiel.de/watch?v=wLpoNNe_74x
Die einzelnen gr..

```html
<!DOCTYPE html>
<html lang="de">
<head>
<meta charset="utf-8">
<title>Zeitwabe Kennzahlen</title>
<link href="https://fonts.googleapis.com/css2?family=Saira+Semi+Condensed:wght@300;400;700&display=swap" rel="stylesheet">
<style>
:root{
  --red:#e30613;
  --green:#8ab82a;
  --yellow:#ffcc00;
  --panel:#737b7e;
  --panel-light:#a0a5a8;
  --before:#f1f2f4;
  --tick:#d8dadc;
  --num:#7d8285;
  --axis:#f4f4f4;
}
*{margin:0;padding:0;box-sizing:border-box}
html,body{width:1200px;height:811px;overflow:hidden;background:#fff}
body{font-family:"Saira Semi Condensed",sans-serif;position:relative}
.before-zone{position:absolute;left:0;top:0;width:341px;height:773px;background:var(--before)}
.switch-mark{position:absolute;left:337px;width:7px;background:var(--tick)}
.row{position:absolute;left:0;width:1200px;height:124px}
.row-line{position:absolute;left:0;top:0;width:1200px;height:7px}
.row-tag{position:absolute;left:0;top:7px;width:159px;height:26px;border-bottom-right-radius:8px;
  color:#fff;font-weight:700;font-size:16px;letter-spacing:.8px;line-height:26px;padding-left:10px}
.row-tag.indent{padding-left:19px}
.red .row-line,.red .row-tag{background:var(--red)}
.green .row-line,.green .row-tag{background:var(--green)}
.yellow .row-line,.yellow .row-tag{background:var(--yellow)}
.col{position:absolute;top:0;width:61px;height:124px;margin-left:-30.5px}
.col::before{content:"";position:absolute;left:30px;top:7px;width:1px;height:24px;background:var(--tick)}
.icon{position:absolute;left:50%;top:var(--ic);width:var(--d);height:var(--d);transform:translate(-50%,-50%);display:block}
.num{position:absolute;left:0;width:61px;top:var(--nc);text-align:center;color:var(--num);
  font-size:12.5px;font-weight:400;line-height:11px;letter-spacing:.3px}
.num small{display:block;font-size:11.5px}
.result{position:absolute;left:1062px;top:0;width:138px;height:124px;background:var(--panel)}
.result-label{position:absolute;left:10px;color:#fff;font-weight:700;font-size:24px;letter-spacing:1px;white-space:nowrap}
.result svg{position:absolute;left:0;top:0}
.axis{position:absolute;left:0;top:742px;width:1062px;height:31px;background:var(--axis)}
.axis span{position:absolute;top:11px;width:61px;margin-left:-30.5px;text-align:center;font-size:8px;color:var(--num)}
.phase{position:absolute;top:773px;height:38px;color:#fff;font-weight:700;font-size:17px;letter-spacing:1.3px;
  line-height:38px;text-align:center}
.phase.before{left:0;width:336px;background:var(--panel-light)}
.phase.after{left:343px;width:719px;background:var(--panel)}
.panel-foot{position:absolute;left:1062px;top:742px;width:138px;height:69px;background:var(--panel)}
</style>
</head>
<body>
<svg width="0" height="0" style="position:absolute" aria-hidden="true">
  <defs>
    <symbol id="i-aperture" viewBox="0 0 40 40">
      <circle cx="20" cy="20" r="20" fill="#e30613"/>
      <g fill="none" stroke="#fff" stroke-width="2">
        <path d="M20 6 Q30 10 28 21"/><path d="M32 12 Q34 24 24 28"/><path d="M34 26 Q26 34 16 30"/>
        <path d="M20 34 Q10 30 12 19"/><path d="M8 28 Q6 16 16 12"/><path d="M6 14 Q14 6 24 10"/>
      </g>
    </symbol>
    <symbol id="i-client" viewBox="0 0 40 40">
      <circle cx="20" cy="20" r="20" fill="#8ab82a"/>
    </symbol>
    <symbol id="i-euro" viewBox="0 0 40 40">
      <circle cx="20" cy="20" r="20" fill="#ffcc00"/>
      <circle cx="20" cy="20" r="15" fill="none" stroke="#fff" stroke-width="2"/>
      <text x="20" y="27" text-anchor="middle" font-size="20" font-weight="700" fill="#fff" font-family="Arial,sans-serif">€</text>
    </symbol>
    <symbol id="i-seat" viewBox="0 0 40 40">
      <circle cx="20" cy="20" r="20" fill="#e30613"/>
      <g fill="none" stroke="#fff" stroke-width="2.4" stroke-linejoin="round">
        <rect x="13" y="9" width="14" height="11" rx="2"/>
        <path d="M17 12v5M20 12v5M23 12v5"/>
        <path d="M9 19v6h22v-6"/><path d="M12 25v6M28 25v6"/>
      </g>
    </symbol>
    <symbol id="i-tick" viewBox="0 0 40 40">
      <circle cx="20" cy="20" r="20" fill="#8ab82a"/>
      <circle cx="20" cy="20" r="15.5" fill="none" stroke="#fff" stroke-width="2.2"/>
      <path d="M14 18l5 5 8-9" fill="none" stroke="#fff" stroke-width="3.4" stroke-linecap="round" stroke-linejoin="round"/>
    </symbol>
    <symbol id="i-horn" viewBox="0 0 40 40">
      <circle cx="20" cy="20" r="20" fill="#ffcc00"/>
      <path d="M8 17h5l12-7v20l-12-7H8z" fill="#fff"/>
      <path d="M12 23l2 7h3l-1-7z" fill="#fff"/>
      <path d="M28 15h4M28 20h5M28 25h4" stroke="#fff" stroke-width="2"/>
    </symbol>
  </defs>
</svg>

<div class="before-zone"></div>

<!-- Shootings -->
<section class="row red" style="top:0;--ic:65px;--nc:102px">
  <div class="row-line"></div><div class="row-tag">SHOOTINGS</div>
  <div class="col" style="left:37px;--d:23px"><svg class="icon"><use href="#i-aperture"/></svg><div class="num" style="top:99px">9</div></div>
  <div class="col" style="left:98px;--d:21px"><svg class="icon"><use href="#i-aperture"/></svg><div class="num">8</div></div>
  <div class="col" style="left:159px;--d:26px"><svg class="icon"><use href="#i-aperture"/></svg><div class="num">10</div></div>
  <div class="col" style="left:219px;--d:23px"><svg class="icon"><use href="#i-aperture"/></svg><div class="num">9</div></div>
  <div class="col" style="left:280px;--d:26px"><svg class="icon"><use href="#i-aperture"/></svg><div class="num">10</div></div>
  <div class="col" style="left:340px;--d:31px"><svg class="icon"><use href="#i-aperture"/></svg><div class="num">12</div></div>
  <div class="col" style="left:403px;--d:34px"><svg class="icon"><use href="#i-aperture"/></svg><div class="num">13</div></div>
  <div class="col" style="left:464px;--d:23px"><svg class="icon"><use href="#i-aperture"/></svg><div class="num">9</div></div>
  <div class="col" style="left:525px;--d:42px"><svg class="icon"><use href="#i-aperture"/></svg><div class="num">16</div></div>
  <div class="col" style="left:585px;--d:49px"><svg class="icon"><use href="#i-aperture"/></svg><div class="num">19</div></div>
  <div class="col" style="left:646px;--d:60px"><svg class="icon"><use href="#i-aperture"/></svg><div class="num">23</div></div>
  <div class="col" style="left:707px;--d:55px"><svg class="icon"><use href="#i-aperture"/></svg><div class="num">21</div></div>
  <div class="col" style="left:768px;--d:47px"><svg class="icon"><use href="#i-aperture"/></svg><div class="num">18</div></div>
  <div class="col" style="left:829px;--d:52px"><svg class="icon"><use href="#i-aperture"/></svg><div class="num">20</div></div>
  <div class="col" style="left:890px;--d:39px"><svg class="icon"><use href="#i-aperture"/></svg><div class="num">15</div></div>
  <div class="col" style="left:951px;--d:31px"><svg class="icon"><use href="#i-aperture"/></svg><div class="num">12</div></div>
  <div class="col" style="left:1012px;--d:65px"><svg class="icon"><use href="#i-aperture"/></svg><div class="num">25</div></div>
  <div class="result">
    <svg width="138" height="124"><path d="M0 97h83l22-47" fill="none" stroke="#fff" stroke-width="3"/><path d="M98 56l8-8 1 11" fill="none" stroke="#fff" stroke-width="3"/></svg>
    <div class="result-label" style="top:52px">+ xx %</div>
  </div>
</section>

<!-- Kunden -->
<section class="row green" style="top:124px;--ic:60px;--nc:100px">
  <div class="row-line"></div><div class="row-tag indent">KUNDEN</div>
  <div class="col" style="left:37px;--d:20px"><svg class="icon"><use href="#i-client"/></svg><div class="num">144</div></div>
  <div class="col" style="left:98px;--d:18px"><svg class="icon"><use href="#i-client"/></svg><div class="num">128</div></div>
  <div class="col" style="left:159px;--d:22px"><svg class="icon"><use href="#i-client"/></svg><div class="num">160</div></div>
  <div class="col" style="left:219px;--d:20px"><svg class="icon"><use href="#i-client"/></svg><div class="num">145</div></div>
  <div class="col" style="left:280px;--d:22px"><svg class="icon"><use href="#i-client"/></svg><div class="num">161</div></div>
  <div class="col" style="left:340px;--d:29px"><svg class="icon"><use href="#i-client"/></svg><div class="num">216</div></div>
  <div class="col" style="left:403px;--d:30px"><svg class="icon"><use href="#i-client"/></svg><div class="num">221</div></div>
  <div class="col" style="left:464px;--d:21px"><svg class="icon"><use href="#i-client"/></svg><div class="num">153</div></div>
  <div class="col" style="left:525px;--d:37px"><svg class="icon"><use href="#i-client"/></svg><div class="num">272</div></div>
  <div class="col" style="left:585px;--d:44px"><svg class="icon"><use href="#i-client"/></svg><div class="num">323</div></div>
  <div class="col" style="left:646px;--d:53px"><svg class="icon"><use href="#i-client"/></svg><div class="num">391</div></div>
  <div class="col" style="left:707px;--d:48px"><svg class="icon"><use href="#i-client"/></svg><div class="num">357</div></div>
  <div class="col" style="left:768px;--d:41px"><svg class="icon"><use href="#i-client"/></svg><div class="num">306</div></div>
  <div class="col" style="left:829px;--d:46px"><svg class="icon"><use href="#i-client"/></svg><div class="num">340</div></div>
  <div class="col" style="left:890px;--d:35px"><svg class="icon"><use href="#i-client"/></svg><div class="num">355</div></div>
  <div class="col" style="left:951px;--d:28px"><svg class="icon"><use href="#i-client"/></svg><div class="num">204</div></div>
  <div class="col" style="left:1012px;--d:57px"><svg class="icon"><use href="#i-client"/></svg><div class="num">425</div></div>
  <div class="result" style="top:7px;height:117px">
    <svg width="138" height="117"><path d="M0 92h83l38-84" fill="none" stroke="#fff" stroke-width="3"/><path d="M114 13l8-8 1 11" fill="none" stroke="#fff" stroke-width="3"/></svg>
    <div class="result-label" style="top:40px">+ xx %</div>
  </div>
</section>

<!-- Umsatz -->
<section class="row yellow" style="top:247px;--ic:63px;--nc:97px">
  <div class="row-line"></div><div class="row-tag indent">UMSATZ</div>
  <div class="col" style="left:37px;--d:30px"><svg class="icon"><use href="#i-euro"/></svg><div class="num">100<small>(Basis)</small></div></div>
  <div class="col" style="left:98px;--d:29px"><svg class="icon"><use href="#i-euro"/></svg><div class="num">97</div></div>
  <div class="col" style="left:159px;--d:29px"><svg class="icon"><use href="#i-euro"/></svg><div class="num">97</div></div>
  <div class="col" style="left:219px;--d:28px"><svg class="icon"><use href="#i-euro"/></svg><div class="num">94</div></div>
  <div class="col" style="left:280px;--d:29px"><svg class="icon"><use href="#i-euro"/></svg><div class="num">97</div></div>
  <div class="col" style="left:340px;--d:31px"><svg class="icon"><use href="#i-euro"/></svg><div class="num">102</div></div>
  <div class="col" style="left:403px;--d:32px"><svg class="icon"><use href="#i-euro"/></svg><div class="num">105</div></div>
  <div class="col" style="left:464px;--d:31px"><svg class="icon"><use href="#i-euro"/></svg><div class="num">102</div></div>
  <div class="col" style="left:525px;--d:32px"><svg class="icon"><use href="#i-euro"/></svg><div class="num">108</div></div>
  <div class="col" style="left:585px;--d:34px"><svg class="icon"><use href="#i-euro"/></svg><div class="num">114</div></div>
  <div class="col" style="left:646px;--d:39px"><svg class="icon"><use href="#i-euro"/></svg><div class="num">131</div></div>
  <div class="col" style="left:707px;--d:38px"><svg class="icon"><use href="#i-euro"/></svg><div class="num">128</div></div>
  <div class="col" style="left:768px;--d:43px"><svg class="icon"><use href="#i-euro"/></svg><div class="num">142</div></div>
  <div class="col" style="left:829px;--d:41px"><svg class="icon"><use href="#i-euro"/></svg><div class="num">137</div></div>
  <div class="col" style="left:890px;--d:47px"><svg class="icon"><use href="#i-euro"/></svg><div class="num">157</div></div>
  <div class="col" style="left:951px;--d:46px"><svg class="icon"><use href="#i-euro"/></svg><div class="num">154</div></div>
  <div class="col" style="left:1012px;--d:52px"><svg class="icon"><use href="#i-euro"/></svg><div class="num">174</div></div>
  <div class="result" style="top:7px;height:117px">
    <svg width="138" height="117"><path d="M0 87h83l26-58" fill="none" stroke="#fff" stroke-width="3"/><path d="M102 34l8-8 1 11" fill="none" stroke="#fff" stroke-width="3"/></svg>
    <div class="result-label" style="top:31px">+ 74 %</div>
  </div>
</section>

<!-- No-Show-Rate -->
<section class="row red" style="top:372px;--ic:74px;--nc:103px">
  <div class="row-line"></div><div class="row-tag">NO-SHOW-RATE</div>
  <div class="col" style="left:37px;--d:52px"><svg class="icon"><use href="#i-seat"/></svg><div class="num">30</div></div>
  <div class="col" style="left:98px;--d:48px"><svg class="icon"><use href="#i-seat"/></svg><div class="num">28</div></div>
  <div class="col" style="left:157px;--d:53px"><svg class="icon"><use href="#i-seat"/></svg><div class="num">31</div></div>
  <div class="col" style="left:221px;--d:46px"><svg class="icon"><use href="#i-seat"/></svg><div class="num">27</div></div>
  <div class="col" style="left:280px;--d:50px"><svg class="icon"><use href="#i-seat"/></svg><div class="num">29</div></div>
  <div class="col" style="left:340px;--d:26px"><svg class="icon"><use href="#i-seat"/></svg><div class="num">15</div></div>
  <div class="col" style="left:403px;--d:24px"><svg class="icon"><use href="#i-seat"/></svg><div class="num">14</div></div>
  <div class="col" style="left:464px;--d:22px"><svg class="icon"><use href="#i-seat"/></svg><div class="num">13</div></div>
  <div class="col" style="left:525px;--d:26px"><svg class="icon"><use href="#i-seat"/></svg><div class="num">15</div></div>
  <div class="col" style="left:585px;--d:22px"><svg class="icon"><use href="#i-seat"/></svg><div class="num">13</div></div>
  <div class="col" style="left:646px;--d:21px"><svg class="icon"><use href="#i-seat"/></svg><div class="num">12</div></div>
  <div class="col" style="left:707px;--d:22px"><svg class="icon"><use href="#i-seat"/></svg><div class="num">13</div></div>
  <div class="col" style="left:768px;--d:21px"><svg class="icon"><use href="#i-seat"/></svg><div class="num">12</div></div>
  <div class="col" style="left:829px;--d:19px"><svg class="icon"><use href="#i-seat"/></svg><div class="num">11</div></div>
  <div class="col" style="left:890px;--d:21px"><svg class="icon"><use href="#i-seat"/></svg><div class="num">12</div></div>
  <div class="col" style="left:951px;--d:22px"><svg class="icon"><use href="#i-seat"/></svg><div class="num">13</div></div>
  <div class="col" style="left:1012px;--d:21px"><svg class="icon"><use href="#i-seat"/></svg><div class="num">12</div></div>
  <div class="result" style="top:7px;height:117px">
    <svg width="138" height="117"><path d="M0 59h83l20 40" fill="none" stroke="#fff" stroke-width="3"/><path d="M92 92l10 8 2-12" fill="none" stroke="#fff" stroke-width="3"/></svg>
    <div class="result-label" style="top:18px">- xx %</div>
  </div>
</section>

<!-- Zeitaufwand -->
<section class="row green" style="top:496px;--ic:63px;--nc:100px">
  <div class="row-line"></div><div class="row-tag indent">ZEITAUFWAND</div>
  <div class="col" style="left:38px;--d:52px"><svg class="icon"><use href="#i-tick"/></svg><div class="num">61</div></div>
  <div class="col" style="left:99px;--d:51px"><svg class="icon"><use href="#i-tick"/></svg><div class="num">60</div></div>
  <div class="col" style="left:160px;--d:53px"><svg class="icon"><use href="#i-tick"/></svg><div class="num">63</div></div>
  <div class="col" style="left:221px;--d:52px"><svg class="icon"><use href="#i-tick"/></svg><div class="num">61</div></div>
  <div class="col" style="left:282px;--d:53px"><svg class="icon"><use href="#i-tick"/></svg><div class="num">63</div></div>
  <div class="col" style="left:342px;--d:10px"><svg class="icon"><use href="#i-tick"/></svg><div class="num">12</div></div>
  <div class="col" style="left:403px;--d:9px"><svg class="icon"><use href="#i-tick"/></svg><div class="num">10</div></div>
  <div class="col" style="left:464px;--d:9px"><svg class="icon"><use href="#i-tick"/></svg><div class="num">11</div></div>
  <div class="col" style="left:525px;--d:10px"><svg class="icon"><use href="#i-tick"/></svg><div class="num">12</div></div>
  <div class="col" style="left:585px;--d:9px"><svg class="icon"><use href="#i-tick"/></svg><div class="num">11</div></div>
  <div class="col" style="left:646px;--d:10px"><svg class="icon"><use href="#i-tick"/></svg><div class="num">12</div></div>
  <div class="col" style="left:707px;--d:9px"><svg class="icon"><use href="#i-tick"/></svg><div class="num">11</div></div>
  <div class="col" style="left:768px;--d:10px"><svg class="icon"><use href="#i-tick"/></svg><div class="num">12</div></div>
  <div class="col" style="left:829px;--d:8px"><svg class="icon"><use href="#i-tick"/></svg><div class="num">10</div></div>
  <div class="col" style="left:890px;--d:7px"><svg class="icon"><use href="#i-tick"/></svg><div class="num">9</div></div>
  <div class="col" style="left:951px;--d:8px"><svg class="icon"><use href="#i-tick"/></svg><div class="num">10</div></div>
  <div class="col" style="left:1012px;--d:10px"><svg class="icon"><use href="#i-tick"/></svg><div class="num">13</div></div>
  <div class="result" style="top:7px;height:117px">
    <svg width="138" height="117"><path d="M0 53h83l28 58" fill="none" stroke="#fff" stroke-width="3"/><path d="M100 104l11 8 1-12" fill="none" stroke="#fff" stroke-width="3"/></svg>
    <div class="result-label" style="top:14px">- xx %</div>
  </div>
</section>

<!-- Werbekosten -->
<section class="row yellow" style="top:620px;--ic:66px;--nc:92px">
  <div class="row-line"></div><div class="row-tag indent">WERBEKOSTEN</div>
  <div class="col" style="left:36px;--d:37px"><svg class="icon"><use href="#i-horn"/></svg><div class="num">100<small>(Basis)</small></div></div>
  <div class="col" style="left:98px;--d:36px"><svg class="icon"><use href="#i-horn"/></svg><div class="num">96</div></div>
  <div class="col" style="left:156px;--d:38px"><svg class="icon"><use href="#i-horn"/></svg><div class="num">103</div></div>
  <div class="col" style="left:220px;--d:37px"><svg class="icon"><use href="#i-horn"/></svg><div class="num">100</div></div>
  <div class="col" style="left:280px;--d:37px"><svg class="icon"><use href="#i-horn"/></svg><div class="num">100</div></div>
  <div class="col" style="left:341px;--d:30px"><svg class="icon"><use href="#i-horn"/></svg><div class="num">80</div></div>
  <div class="col" style="left:403px;--d:27px"><svg class="icon"><use href="#i-horn"/></svg><div class="num">70</div></div>
  <div class="col" style="left:464px;--d:26px"><svg class="icon"><use href="#i-horn"/></svg><div class="num">67</div></div>
  <div class="col" style="left:525px;--d:26px"><svg class="icon"><use href="#i-horn"/></svg><div class="num">67</div></div>
  <div class="col" style="left:585px;--d:25px"><svg class="icon"><use href="#i-horn"/></svg><div class="num">63</div></div>
  <div class="col" style="left:646px;--d:25px"><svg class="icon"><use href="#i-horn"/></svg><div class="num">63</div></div>
  <div class="col" style="left:707px;--d:26px"><svg class="icon"><use href="#i-horn"/></svg><div class="num">67</div></div>
  <div class="col" style="left:768px;--d:27px"><svg class="icon"><use href="#i-horn"/></svg><div class="num">70</div></div>
  <div class="col" style="left:829px;--d:26px"><svg class="icon"><use href="#i-horn"/></svg><div class="num">67</div></div>
  <div class="col" style="left:890px;--d:23px"><svg class="icon"><use href="#i-horn"/></svg><div class="num">60</div></div>
  <div class="col" style="left:951px;--d:25px"><svg class="icon"><use href="#i-horn"/></svg><div class="num">63</div></div>
  <div class="col" style="left:1012px;--d:26px"><svg class="icon"><use href="#i-horn"/></svg><div class="num">67</div></div>
  <div class="result" style="top:7px;height:115px">
    <svg width="138" height="115"><path d="M0 73h83l18 38" fill="none" stroke="#fff" stroke-width="3"/><path d="M90 104l11 8 1-12" fill="none" stroke="#fff" stroke-width="3"/></svg>
    <div class="result-label" style="top:28px">- 33 %</div>
  </div>
</section>

<div class="switch-mark" style="top:7px;height:24px"></div>
<div class="switch-mark" style="top:131px;height:24px"></div>
<div class="switch-mark" style="top:254px;height:24px"></div>
<div class="switch-mark" style="top:379px;height:24px"></div>
<div class="switch-mark" style="top:503px;height:24px"></div>
<div class="switch-mark" style="top:627px;height:24px"></div>

<div class="axis">
  <span style="left:37px">Mai 17</span><span style="left:98px">Juni 17</span><span style="left:159px">Juli 17</span>
  <span style="left:219px">Aug 17</span><span style="left:280px">Sep 17</span><span style="left:340px">Okt 17</span>
  <span style="left:403px">Nov17</span><span style="left:464px">Dez 17</span><span style="left:525px">Jan 18</span>
  <span style="left:585px">Feb 18</span><span style="left:646px">Mär 18</span><span style="left:707px">Apr 18</span>
  <span style="left:768px">Mai 18</span><span style="left:829px">Jun 18</span><span style="left:890px">Jul 18</span>
  <span style="left:951px">Aug 18</span><span style="left:1012px">Sep 18</span>
</div>
<div class="panel-foot"></div>
<div class="phase before">OHNE TERMIN-TOOL</div>
<div class="phase after">NUTZUNG ZEITWABE UND LOBPUNKT</div>
</body>
</html>
```